Advertising tiles for website

Hi
I have a website at www.tagwhistle.co.nz and there are four spots along the top for advertising tiles (at the moment there are dummy tiles in place).

Each tile is 220 wide and 200 high and I would like 4 tiles created as a starting point for this site.

I can change the tiles on every page so conceivably we could have very targeted advertising leading the visitor to services we want to promote (we can set this extension up as a new design job for you). Eg. domains for sale, Escrow services, featured domains, Turnkey Websites, New Websites etc.

The advertisements that I might like see on the website would be as follows:
Gallery Ink
Sell Your Domain
Domains For Sale
Featured Domains
Buy Websites
Sell Your Website
Turnkey Websites
Trusted Escrow
New domains
News
Resources
note: the deliverable for this job is 4 tiles (not all of the above)as I want to get the design style sorted with you.

The website where these will appear sells pre-loved domains and turnkey websites. Also, some of these tiles will link through to a classifieds website which we will also want you to help create tiles for once this job is completed to satisfaction.

The files attached are samples only.

Target Market(s)

Domain buyers
Business owners
People buying websites

Industry/Entity Type

Advertising

Requirements
Must have
• Nice clean, clear text
Relevant
Nice to have
• Fun

```html
<!DOCTYPE html>
<html lang="en">
<head>
<meta charset="utf-8">
<title>Advertising Tiles</title>
<link rel="stylesheet" href="https://fonts.googleapis.com/css2?family=Quicksand:wght@400;500&display=swap">
<style>
  :root {
    --page: #ffffff;
    --ink: #ffffff;
    --sell-light: #e0245a;
    --sell-dark: #a80d35;
    --featured-light: #9b46c4;
    --featured-dark: #5e1f86;
    --news-light: #2f8fd8;
    --news-dark: #0b2c5c;
    --buy-light: #f29a2a;
    --buy-dark: #d4540c;
  }
  html, body {
    margin: 0;
    padding: 0;
    width: 1141px;
    height: 1200px;
    overflow: hidden;
    background: var(--page);
  }
  .tile-board {
    position: relative;
    width: 1141px;
    height: 1200px;
    font-family: "Quicksand", sans-serif;
    color: var(--ink);
  }
  .tile {
    position: absolute;
    width: 502px;
    height: 458px;
    display: flex;
    flex-direction: column;
    align-items: center;
    justify-content: center;
    overflow: hidden;
    text-align: center;
    line-height: 1;
  }
  .tile--sell {
    left: 39px; top: 119px;
    background:
      radial-gradient(circle at 82% 30%, rgba(255,255,255,0.18) 0 40px, transparent 42px),
      radial-gradient(circle at 70% 80%, rgba(255,255,255,0.12) 0 60px, transparent 62px),
      radial-gradient(ellipse at 60% 40%, var(--sell-light), var(--sell-dark) 80%);
  }
  .tile--featured {
    left: 589px; top: 119px;
    background:
      radial-gradient(circle at 80% 25%, rgba(255,255,255,0.16) 0 30px, transparent 32px),
      radial-gradient(circle at 30% 75%, rgba(255,255,255,0.1) 0 50px, transparent 52px),
      radial-gradient(ellipse at 65% 35%, var(--featured-light), var(--featured-dark) 85%);
  }
  .tile--news {
    left: 39px; top: 612px;
    background: #081a38;
  }
  .tile--buy {
    left: 589px; top: 612px;
    background:
      radial-gradient(circle at 20% 30%, rgba(255,255,255,0.16) 0 35px, transparent 37px),
      radial-gradient(circle at 78% 65%, rgba(255,255,255,0.12) 0 55px, transparent 57px),
      radial-gradient(ellipse at 50% 40%, var(--buy-light), var(--buy-dark) 85%);
  }
  .world-backdrop {
    position: absolute;
    inset: 0;
    background: radial-gradient(ellipse at 50% 45%, var(--news-light), var(--news-dark) 80%);
  }
  .tile__headline, .tile__subline { position: relative; font-weight: 400; }
  .tile--sell .tile__headline { font-size: 215px; letter-spacing: 2px; margin-top: -20px; }
  .tile--sell .tile__subline { font-size: 52px; margin-top: 12px; }
  .tile--featured .tile__headline { font-size: 92px; letter-spacing: 3px; line-height: 1.2; }
  .tile--news .tile__headline { font-size: 132px; letter-spacing: 3px; }
  .tile--buy .tile__headline { font-size: 225px; letter-spacing: 2px; margin-top: -20px; }
  .tile--buy .tile__subline { font-size: 78px; letter-spacing: 3px; margin-top: 8px; }
</style>
</head>
<body>
  <main class="tile-board">
    <section class="tile tile--sell">
      <div class="tile__headline">Sell</div>
      <div class="tile__subline">Your Domain</div>
    </section>
    <section class="tile tile--featured">
      <div class="tile__headline">Featured<br>Domains</div>
    </section>
    <section class="tile tile--news">
      <div class="world-backdrop" role="img" aria-label="Glowing blue world map on a dark grid background"></div>
      <div class="tile__headline">News</div>
    </section>
    <section class="tile tile--buy">
      <div class="tile__headline">Buy</div>
      <div class="tile__subline">Websites</div>
    </section>
  </main>
</body>
</html>
```